Website Re-design

Hi, I'm looking for help in redesigning my web site. I currently have a site www.brightnookwares.example where I sell lamps, and while I like some aspects of the design, you can tell that I have done the graphics myself and am not a pro at it. I'd like help in redesigning it, and am open to completely new design graphics. I have made the 3 slider images myself, and I feel they could be a bit better, but I am not sure how to do it. For example, on the homepage, the 'About Us', 'Secured Shopping', and '$10 Off' graphics don't go well with the rest of the page. I would like more cohesion in the design and more visual interest in the header, which is pretty basic right now. Also, that the bottom footer is black, I would like instead something else. I am looking for just the layout of the homepage, and possibly once that is done to work on more visual interest in some of the informational pages and product pages. I am looking for just the design in the form of a photoshop file or files that I can incorporate into my site. Thank you!

Reason: I just made this project payment committed, so I'd like a chance for designers who only choose payment committed projects to submit artwork. Thank you.

This project is now payment guaranteed/ committed.  Thanks.

```html
<!DOCTYPE html>
<html lang="en">
<head>
<meta charset="utf-8">
<title>Bright Nook — Home</title>
<link rel="stylesheet" href="https://fonts.googleapis.com/css2?family=Montserrat:wght@300;400;500;600;700&display=swap">
<style>
  :root {
    --orange: #ff8a00;
    --yellow: #ffc400;
    --ink: #3a3a3a;
    --ink-soft: #555555;
    --muted: #777777;
    --band: #f1f1f1;
    --white: #ffffff;
    --rule: #e2e2e2;
    --black: #111111;
  }
  * { box-sizing: border-box; margin: 0; padding: 0; }
  html, body { width: 1133px; height: 1200px; overflow: hidden; }
  body {
    position: relative;
    background: var(--white);
    font-family: "Montserrat", sans-serif;
    color: var(--ink);
  }
  a { color: inherit; text-decoration: none; }

  .utility-bar {
    position: absolute; left: 0; top: 0; width: 1133px; height: 45px;
    background: var(--band);
    font-size: 12px; font-weight: 300; color: var(--muted);
  }
  .utility-bar .account-links { position: absolute; left: 557px; top: 15px; white-space: nowrap; }
  .utility-bar .sep { margin: 0 20px; }
  .btn-cart, .btn-checkout {
    position: absolute; top: 11px; height: 25px; width: 79px;
    color: var(--white); font-size: 12px; font-weight: 600;
    display: flex; align-items: center; justify-content: center;
  }
  .btn-cart { left: 859px; background: var(--orange); }
  .btn-checkout { left: 942px; width: 81px; background: var(--yellow); }

  .site-header { position: absolute; left: 0; top: 45px; width: 1133px; height: 73px; background: var(--white); }
  .brand { position: absolute; left: 116px; top: 16px; display: flex; align-items: center; gap: 10px; }
  .brand-mark { width: 34px; height: 34px; border: 3px solid var(--ink); border-radius: 50%; }
  .brand-name { font-size: 23px; font-weight: 500; color: var(--ink); line-height: 1; }
  .main-nav { position: absolute; top: 32px; font-size: 14px; font-weight: 500; color: var(--ink); }
  .main-nav a { position: absolute; white-space: nowrap; }

  .hero-band { position: absolute; left: 0; top: 118px; width: 1133px; height: 504px; background: var(--band); }
  .hero {
    position: absolute; left: 114px; top: 26px; width: 906px; height: 430px;
    background:
      linear-gradient(180deg, transparent 0 72%, #c9d3d4 72%, #dfe5e5 100%),
      linear-gradient(90deg, #2f8f94 0%, #5fbcbf 45%, #9fe0e0 75%, #b7eaea 100%);
  }
  .hero-copy { position: absolute; left: 0; top: 0; width: 456px; text-align: center; color: var(--white); }
  .hero-kicker { position: absolute; left: 0; width: 456px; top: 86px; font-size: 35px; font-weight: 300; white-space: nowrap; }
  .hero-title { position: absolute; left: 0; width: 456px; top: 148px; font-size: 35px; font-weight: 600; white-space: nowrap; }
  .hero-sub { position: absolute; left: 0; width: 456px; top: 199px; font-size: 22px; font-weight: 400; }
  .hero-cta {
    position: absolute; left: 141px; top: 231px; width: 172px; height: 41px;
    background: var(--orange); color: var(--white); font-size: 15px; font-weight: 400;
    display: flex; align-items: center; justify-content: center; gap: 8px;
  }
  .slider-dots { position: absolute; top: 468px; left: 516px; display: flex; gap: 7px; }
  .slider-dots span { width: 14px; height: 14px; background: var(--black); }
  .slider-dots span.active { background: var(--orange); }

  .feature { position: absolute; top: 666px; width: 300px; }
  .feature h2 { font-size: 17px; font-weight: 600; color: var(--ink); letter-spacing: .3px; height: 24px; }
  .feature-photo { width: 283px; height: 132px; margin-top: 11px; }
  .feature p { width: 285px; font-size: 12px; font-weight: 400; line-height: 20px; color: var(--ink-soft); margin-top: 15px; }
  .feature .more { display: block; font-size: 11px; font-weight: 600; color: var(--ink-soft); margin-top: 2px; }
  .photo-about { background: linear-gradient(120deg, #c8643e, #a43e1e); }
  .photo-secure { background: linear-gradient(120deg, #e7dcd2, #d8e2ea 60%, #a9d7dc); }
  .photo-offer { background: linear-gradient(90deg, #6b4a22 0%, #2a1c0c 30%, #000 55%); }

  .site-footer { position: absolute; left: 0; top: 937px; width: 1133px; height: 213px; background: var(--band); border-bottom: 1px solid var(--rule); }
  .footer-col { position: absolute; top: 33px; }
  .footer-col h3 { font-size: 13px; font-weight: 600; color: var(--black); margin-bottom: 20px; }
  .footer-col li { list-style: none; font-size: 11.5px; font-weight: 400; color: var(--ink-soft); line-height: 20.5px; white-space: nowrap; }
  .social { position: absolute; top: 39px; left: 901px; display: flex; gap: 7px; }
  .social span { width: 30px; height: 30px; border-radius: 50%; background: var(--black); }
  .newsletter-field {
    position: absolute; left: 707px; top: 80px; width: 302px; height: 35px;
    background: var(--white); border: 2px solid #e6e6e6;
    font-size: 11.5px; font-weight: 300; color: #999; padding: 9px 13px; white-space: nowrap;
  }
  .copyright { position: absolute; left: 0; top: 1165px; width: 1133px; text-align: center; font-size: 12px; color: var(--ink); }
</style>
</head>
<body>
  <div class="utility-bar">
    <div class="account-links"><a href="#">Sign in or Create an account</a><span class="sep">|</span><a href="#">My Account</a><span class="sep">|</span></div>
    <a class="btn-cart" href="#">View Cart</a>
    <a class="btn-checkout" href="#">Checkout</a>
  </div>

  <header class="site-header">
    <a class="brand" href="#"><span class="brand-mark"></span><span class="brand-name">bright nook</span></a>
    <nav class="main-nav">
      <a href="#" style="left:638px">HOME</a>
      <a href="#" style="left:723px">SHOP</a>
      <a href="#" style="left:817px">ABOUT US</a>
      <a href="#" style="left:929px">CONTACT US</a>
    </nav>
  </header>

  <section class="hero-band">
    <div class="hero" role="img" aria-label="Teal wall and white wooden floor with a blue glass table lamp with white shade">
      <div class="hero-copy">
        <div class="hero-kicker">Light Up the room</div>
        <div class="hero-title">“THE MARINA ”</div>
        <div class="hero-sub">Medium Table lamp</div>
        <a class="hero-cta" href="#">SHOP ALL LAMPS
          <svg width="12" height="18" viewBox="0 0 12 18"><path d="M2 2 L9 9 L2 16" fill="none" stroke="#fff" stroke-width="3.5"/></svg>
        </a>
      </div>
    </div>
    <div class="slider-dots"><span class="active"></span><span></span><span></span></div>
  </section>

  <section class="feature" style="left:122px">
    <h2>ABOUT US</h2>
    <div class="feature-photo photo-about" role="img" aria-label="Wall sconce with pleated shade on a warm orange wall"></div>
    <p style="margin-left:-4px; width:270px">Bright Nook provides beautiful and artistic home and hospitality lighting.</p>
    <a class="more" href="#" style="margin-left:-4px">READ MORE &gt;&gt;</a>
  </section>
  <section class="feature" style="left:425px">
    <h2 style="margin-left:2px">SECURED SHOPPING</h2>
    <div class="feature-photo photo-secure" role="img" aria-label="Shopper holding bags and a phone"></div>
    <p>Shopping at Bright Nook is secured and protected by industry standard best practices.</p>
    <a class="more" href="#">READ MORE &gt;&gt;</a>
  </section>
  <section class="feature" style="left:727px">
    <h2>$ 10 OFF</h2>
    <div class="feature-photo photo-offer" role="img" aria-label="Lit pleated lamp shade against a dark background"></div>
    <p style="font-size:13.5px">$10 off any purchase when you sign up for our newsletter.</p>
    <a class="more" href="#">SIGN UP &gt;&gt;</a>
  </section>

  <footer class="site-footer">
    <div class="footer-col" style="left:123px"><h3>Help + Info</h3><ul><li>Contact Us</li><li>Shipping Info</li><li>Returns</li><li>To The Trade</li><li>Privacy Policy</li><li>Terms of Use</li></ul></div>
    <div class="footer-col" style="left:265px"><h3>My Account</h3><ul><li>Sign In</li><li>Order Status</li><li>Order History</li><li>View Cart</li><li>Checkout</li></ul></div>
    <div class="footer-col" style="left:406px"><h3>About Us</h3><ul><li>Who we are ?</li><li>Testimonials</li></ul></div>
    <div class="footer-col" style="left:532px"><h3>Contact</h3><ul><li>Contact Us</li><li>info@brightnook.example</li></ul></div>
    <div class="social"><span></span><span></span><span></span></div>
    <div class="newsletter-field">Enter E-Mail for news,Sales and executives</div>
  </footer>

  <div class="copyright">© Bright Nook 2013 | All Rights Reserved</div>
</body>
</html>
```